Cloud Hosted Phone System for small and medium sized businesses

I want to design a one A4 page size single or double sided brochure to offer cloud hosted VoIP Phone system and a complete collaboration system. We have partnered with a VoIP Phone system company and want to sell their services but we don't want their name to be shown on the brochure because customers might call them directly. The company name is Zelvora (www.zelvora-example.com) and our company name is HALCYON Tech Solutions. I have also uploaded my compnay's logo that you should show on the brochure. For more details about the product, you can visit their website as mentioned above.

Target Market(s)

Small and medium sized business including law firms, marketing and advertising agencies, real-estate firms and others.

Industry/Entity Type

Voip

Colors

Designer to choose colors to be used in the design.

Requirements
Must have
• My company's Logo (HALCYON Tech Solutions). Price list, services and some images to show the benefits and services of the cloud based and advanced VoIP phone system. I want the brochure to look very professional and attractive.
• Contact US: Our company's name, Logo, web address, phone (416-557-9086) and email (info@halcyontechsolutions-example.com)
Nice to have
• It is a Canadian based company and all of our servers and customers’ data reside in Canada.

```html
<!DOCTYPE html>
<html lang="en">
<head>
<meta charset="utf-8">
<title>HALCYON Tech Solutions – Cloud-Based Phone System Brochure</title>
<link rel="stylesheet" href="https://fonts.googleapis.com/css2?family=Raleway:wght@400;500;600;700&family=Roboto+Condensed:wght@400;700&display=swap">
<style>
:root{
  --blue:#2463ad;
  --blue-deep:#1a4f96;
  --blue-band:#1d5aa6;
  --blue-head:#3a78be;
  --blue-head-strong:#1c5ba8;
  --cell:#d9e5f2;
  --cell-strong:#c5d6ea;
  --row-dark:#3b3b3e;
  --ink:#2b2b2b;
  --black:#0c0d12;
  --white:#ffffff;
  --stage:#e9ebee;
}
*{box-sizing:border-box;margin:0;padding:0}
html,body{width:1200px;height:854px;overflow:hidden;background:var(--stage)}
body{position:relative;font-family:"Raleway",Arial,sans-serif;color:var(--ink)}
.page{position:absolute;top:54px;width:528px;height:746px;background:var(--white);overflow:hidden;box-shadow:0 2px 10px rgba(0,0,0,.18)}
.page--pricing{left:53px}
.page--overview{left:620px}
.abs{position:absolute}

/* ---------- pricing page ---------- */
.hero-band{left:0;top:0;width:528px;height:214px;background:linear-gradient(180deg,#2d6ab3 0%,#2463ad 70%,#2f6db3 100%)}
.hero-title{left:38px;top:38px;width:452px;color:var(--white);font-weight:600;font-size:17.4px;letter-spacing:-.2px;white-space:nowrap;padding-bottom:4px;border-bottom:1px solid rgba(255,255,255,.8)}
.service{top:64px;width:104px}
.service__badge{position:relative;height:52px}
.service__badge svg{position:absolute;left:0;top:0}
.service__label{position:absolute;left:46px;top:10px;font-family:"Roboto Condensed",Arial,sans-serif;font-weight:700;font-size:10.4px;line-height:10.8px;color:var(--blue-head-strong);text-transform:uppercase}
.service__label small{font-size:6px;font-weight:400;display:block;line-height:9px}
.service__text{margin-top:4px;color:var(--white);font-size:10.4px;line-height:12.8px;text-align:justify;text-align-last:left}

.plans-title{left:38px;top:264px;color:var(--blue-head-strong);font-weight:700;font-size:21px;letter-spacing:-.3px}
.tab{top:261px;height:31px;width:89px;background:var(--blue-head);color:var(--white);font-weight:600;font-size:11.5px;display:flex;align-items:center;justify-content:center;border-radius:8px 8px 0 0}
.tab--strong{background:var(--blue-head-strong)}
.best-seller{left:335px;top:231px;width:37px;height:37px;border-radius:50%;background:var(--blue-head-strong);border:2px solid var(--white);color:var(--white);font-weight:700;font-size:6.6px;line-height:7.4px;text-align:center;display:flex;align-items:center;justify-content:center}
.row-label{left:38px;width:175px;height:21px;background:var(--row-dark);color:var(--white);font-size:9.5px;display:flex;align-items:center;padding-left:6px;white-space:nowrap}
.row-label small{font-size:6.6px;margin-left:3px}
.row-label--accent{background:var(--blue-head-strong)}
.cell{width:89px;height:21px;background:var(--cell);font-weight:700;font-size:9.4px;display:flex;align-items:center;padding-left:28px;color:#222}
.cell--strong{background:var(--cell-strong)}

.features-art{left:0;top:470px}
.features-title{left:0;top:536px;width:528px;text-align:center;color:var(--white);font-weight:600;font-size:17.4px;letter-spacing:-.3px}
.features-title span{border-bottom:1px solid rgba(255,255,255,.8);padding:0 2px 2px}
.feature-list{top:572px;list-style:none;color:var(--white);font-size:10.6px;line-height:11px}
.feature-list li{position:relative;padding-left:13px;margin-bottom:4.2px}
.feature-list li::before{content:"\2713";position:absolute;left:0;top:0;font-size:10px}
.footer-line{left:0;top:706px;width:528px;height:40px;background:var(--white);font-size:10.4px;color:var(--ink);padding:14px 0 0 38px;white-space:nowrap}

/* ---------- overview page ---------- */
.sky-photo{left:0;top:0;width:528px;height:200px;background:linear-gradient(160deg,#9fb9d6 0%,#d7e3ef 35%,#aec5de 60%,#5f84b2 100%)}
.overview-art{left:0;top:0}
.brand{left:272px;top:28px;display:flex;align-items:flex-start;gap:8px}
.brand__dot{width:46px;height:46px;border-radius:50%;background:var(--blue-head-strong);margin-top:6px}
.brand__name{font-weight:500;font-size:33px;line-height:36px;color:#1d2a3a;letter-spacing:.5px}
.brand__sub{font-weight:500;font-size:17px;line-height:18px;color:#1d2a3a;padding-left:4px}
.overview-title{left:70px;top:156px;width:270px;text-align:center;color:var(--blue-head-strong);font-weight:600;font-size:17.6px;line-height:22px;letter-spacing:-.3px}
.overview-intro{left:38px;top:211px;width:400px;font-size:10.3px;line-height:12.8px;text-align:justify;color:#222}
.benefits-title{left:90px;top:308px;width:348px;color:var(--blue-head-strong);font-weight:600;font-size:15.6px;letter-spacing:-.3px;border-bottom:1px solid var(--blue-head-strong);padding-bottom:2px;white-space:nowrap}
.benefit-pill{height:28px;border-radius:14px;background:var(--blue-head-strong);color:var(--white);font-family:"Roboto Condensed",Arial,sans-serif;font-size:7px;line-height:7.6px;font-weight:700;display:flex;align-items:center;gap:4px;padding:0 6px 0 2px;text-transform:uppercase}
.benefit-pill i{width:24px;height:24px;border-radius:50%;background:var(--white);border:2px solid #cfdcec;flex:none}
.diagram-lines{left:0;top:0}
.datacenter{left:124px;top:418px;width:276px;height:106px;background:linear-gradient(180deg,#d8e4f1 0%,#6f7681 45%,#2e3238 100%);border-radius:4px}
.detail-band{left:0;top:535px;width:528px;height:211px;background:linear-gradient(180deg,#2a68b1 0%,var(--blue-band) 100%)}
.detail{top:561px;width:140px;color:var(--white)}
.detail h3,.detail-wide h3{font-size:10.6px;font-weight:600;letter-spacing:-.1px;margin-bottom:2px;display:flex;justify-content:space-between;align-items:center}
.detail p,.detail-wide p{font-size:7.5px;line-height:9.6px;text-align:justify;text-align-last:left}
.detail-wide{left:38px;top:660px;width:452px;color:var(--white)}
</style>
</head>
<body>

<!-- ================= PRICING SIDE ================= -->
<section class="page page--pricing">
  <div class="abs hero-band"></div>
  <h1 class="abs hero-title">A CLOUD-BASED PHONE SYSTEM FOR BUSINESSES</h1>

  <div class="abs service" style="left:38px">
    <div class="service__badge">
      <svg width="104" height="52" viewBox="0 0 104 52"><path d="M24 2h36a14 14 0 0 1 27 6a17 17 0 0 1 0 42H24a24 24 0 0 1 0-48z" fill="#fff"/><circle cx="24" cy="26" r="19" fill="#fff" stroke="#d5dfeb" stroke-width="2"/><rect x="17" y="19" width="14" height="14" rx="2" fill="#2b2b2b"/><rect x="19" y="21" width="10" height="4" fill="#fff"/><g fill="#fff"><rect x="19" y="27" width="2" height="2"/><rect x="23" y="27" width="2" height="2"/><rect x="27" y="27" width="2" height="2"/></g></svg>
      <span class="service__label">Cloud<br>Phone<br>System</span>
    </div>
    <p class="service__text">Your business phone system, now in the cloud. Access every feature from anywhere.</p>
  </div>
  <div class="abs service" style="left:154px">
    <div class="service__badge">
      <svg width="104" height="52" viewBox="0 0 104 52"><path d="M24 2h36a14 14 0 0 1 27 6a17 17 0 0 1 0 42H24a24 24 0 0 1 0-48z" fill="#fff"/><circle cx="24" cy="26" r="19" fill="#fff" stroke="#d5dfeb" stroke-width="2"/><rect x="15" y="19" width="12" height="9" rx="1" fill="none" stroke="#2b2b2b" stroke-width="1.6"/><rect x="21" y="24" width="12" height="9" rx="1" fill="#fff" stroke="#2b2b2b" stroke-width="1.6"/></svg>
      <span class="service__label" style="top:16px">Unified<small>Communications</small></span>
    </div>
    <p class="service__text">A powerful suite of communications and collaboration tools grouped under one platform.</p>
  </div>
  <div class="abs service" style="left:270px">
    <div class="service__badge">
      <svg width="104" height="52" viewBox="0 0 104 52"><path d="M24 2h36a14 14 0 0 1 27 6a17 17 0 0 1 0 42H24a24 24 0 0 1 0-48z" fill="#fff"/><circle cx="24" cy="26" r="19" fill="#fff" stroke="#d5dfeb" stroke-width="2"/><circle cx="24" cy="23" r="6" fill="#2b2b2b"/><path d="M16 36a8 7 0 0 1 16 0z" fill="#2b2b2b"/><path d="M17 23a7 7 0 0 1 14 0" fill="none" stroke="#2b2b2b" stroke-width="1.6"/></svg>
      <span class="service__label" style="top:16px">Contact<br>Center</span>
    </div>
    <p class="service__text">Manage your different customer contact points from a unified. User-friendly web interface.</p>
  </div>
  <div class="abs service" style="left:386px">
    <div class="service__badge">
      <svg width="104" height="52" viewBox="0 0 104 52"><path d="M24 2h36a14 14 0 0 1 27 6a17 17 0 0 1 0 42H24a24 24 0 0 1 0-48z" fill="#fff"/><circle cx="24" cy="26" r="19" fill="#fff" stroke="#d5dfeb" stroke-width="2"/><g stroke="#2b2b2b" stroke-width="1.6" fill="none"><path d="M18 19v14M18 26h6M24 21h8M24 31h8M24 21v10"/></g><g fill="#2b2b2b"><circle cx="18" cy="19" r="2"/><circle cx="32" cy="21" r="2"/><circle cx="32" cy="31" r="2"/></g></svg>
      <span class="service__label" style="top:16px">Meet<br>Studio</span>
    </div>
    <p class="service__text">A flexible yet easy-to-use online administration portal to manage your business phone system.</p>
  </div>

  <h2 class="abs plans-title">SERVICE PLANS</h2>
  <div class="abs tab" style="left:216px">BASIC</div>
  <div class="abs tab tab--strong" style="left:309px">ENHANCED</div>
  <div class="abs tab" style="left:401px">PREMIUM</div>
  <div class="abs best-seller">BEST<br>SELLER</div>

  <div class="abs row-label" style="top:293px">MONTHLY ACCOUNT FEE¹<small>(PER SITE)</small></div>
  <div class="abs row-label row-label--accent" style="top:318px">MONTHLY USER FEE Starting at:</div>
  <div class="abs row-label" style="top:342px">0 to 19 users</div>
  <div class="abs row-label" style="top:366px">20 to 49 users</div>
  <div class="abs row-label" style="top:391px">50 to 99 users</div>
  <div class="abs row-label" style="top:415px">100 to 199 users</div>
  <div class="abs row-label" style="top:439px">200+ users</div>

  <div class="abs cell" style="left:216px;top:293px">$ 45,00</div>
  <div class="abs cell cell--strong" style="left:309px;top:293px">$ 45,00</div>
  <div class="abs cell" style="left:401px;top:293px">$ 45,00</div>

  <div class="abs cell" style="left:216px;top:342px">$ 18,00</div>
  <div class="abs cell cell--strong" style="left:309px;top:342px">$ 20,00</div>
  <div class="abs cell" style="left:401px;top:342px">$ 22,00</div>
  <div class="abs cell" style="left:216px;top:366px">$ 15,00</div>
  <div class="abs cell cell--strong" style="left:309px;top:366px">$ 17,00</div>
  <div class="abs cell" style="left:401px;top:366px">$ 19,00</div>
  <div class="abs cell" style="left:216px;top:391px">$ 12,00</div>
  <div class="abs cell cell--strong" style="left:309px;top:391px">$ 14,00</div>
  <div class="abs cell" style="left:401px;top:391px">$ 16,00</div>
  <div class="abs cell" style="left:216px;top:415px">$ 10,00</div>
  <div class="abs cell cell--strong" style="left:309px;top:415px">$ 12,00</div>
  <div class="abs cell" style="left:401px;top:415px">$ 14,00</div>
  <div class="abs cell" style="left:216px;top:439px">$ 8,00</div>
  <div class="abs cell cell--strong" style="left:309px;top:439px">$ 10,00</div>
  <div class="abs cell" style="left:401px;top:439px">$ 12,00</div>

  <svg class="abs features-art" width="528" height="236" viewBox="0 0 528 236">
    <path d="M0 28C160 6 380 0 528 12V236H0Z" fill="#2463ad"/>
    <path d="M150 14C300-2 440 4 528 24V58C440 30 300 24 170 36C110 42 50 52 0 64V44C50 30 100 20 150 14Z" fill="#0c0d12"/>
    <path d="M0 64C50 52 110 42 170 36C300 24 440 30 528 58V236H0Z" fill="#1d5aa6"/>
  </svg>
  <h2 class="abs features-title"><span>INCLUDED FEATURES</span></h2>
  <ul class="abs feature-list" style="left:38px;width:140px">
    <li>Access to our online portal</li>
    <li>Company greeting message (24h/7)</li>
    <li>Company's directory</li>
    <li>Company and user voicemail</li>
    <li>Outbound Caller ID</li>
    <li>Voicemail to email</li>
  </ul>
  <ul class="abs feature-list" style="left:191px;width:145px">
    <li>Call Forwarding</li>
    <li>Find-me/Follow-me</li>
    <li>Call waiting</li>
    <li>Automatic phone relocation</li>
    <li>Remote office calling &amp; transfering</li>
    <li>Phone queueing service</li>
  </ul>
  <ul class="abs feature-list" style="left:345px;width:150px">
    <li>Fraud Monitoring</li>
    <li>Custom Music on Hold</li>
    <li>Optional Hidden Caller ID</li>
    <li>Authorization code before dialing</li>
    <li>Remote Answer</li>
    <li>Call recording ...and more!</li>
  </ul>
  <p class="abs footer-line">PHONE: 416-557-9086 | SERVICE AREA: Proudly Serving Clients In Toronto &amp; Surrounding Areas</p>
</section>

<!-- ================= OVERVIEW SIDE ================= -->
<section class="page page--overview">
  <div class="abs sky-photo" role="img" aria-label="Photo of glass office towers against a bright cloudy blue sky"></div>
  <svg class="abs overview-art" width="528" height="320" viewBox="0 0 528 320">
    <path d="M0 140C150 80 350 78 528 118V160C350 112 150 116 0 186Z" fill="#1d5aa6"/>
    <path d="M0 186C150 116 350 112 528 160V320H0Z" fill="#fff"/>
    <path d="M300 128C420 140 500 190 528 250V275C490 205 410 160 300 132Z" fill="#0c0d12"/>
    <path d="M340 150C440 165 505 210 528 275V295C495 230 430 180 340 154Z" fill="#1d5aa6"/>
  </svg>
  <div class="abs brand">
    <span class="brand__dot"></span>
    <div>
      <div class="brand__name">HALCYON</div>
      <div class="brand__sub">Tech Solutions</div>
    </div>
  </div>
  <h1 class="abs overview-title">A CLOUD-BASED PHONE<br>SYSTEM FOR BUSINESSES</h1>
  <p class="abs overview-intro">We can help you grow your business by modernizing your company's phone system and making it easy to use, manage, and track directly from the cloud. Our cloud business phone system adapts to your economic challenges and brings flexibility and adaptability to your business communications whilst considerably reducing costs compared to traditional phone systems. We take great pride in continually improving our platform as well as developing new features and services that in turn increase our customers' productivity.</p>
  <h2 class="abs benefits-title">BENEFITS OF CLOUD-BASED PHONE SYSTEM</h2>

  <svg class="abs diagram-lines" width="528" height="530" viewBox="0 0 528 530">
    <g stroke="#2463ad" stroke-width="1" stroke-dasharray="2 2" fill="none">
      <path d="M160 370V424"/><path d="M224 398V424"/><path d="M283 368V424"/><path d="M344 398V424"/>
    </g>
  </svg>
  <div class="abs datacenter" role="img" aria-label="Illustration of server racks in a data center with a laptop showing a cloud icon"></div>
  <div class="abs benefit-pill" style="left:129px;top:342px"><i></i>Become<br>Mobile</div>
  <div class="abs benefit-pill" style="left:250px;top:340px"><i></i>Stay<br>Abreast</div>
  <div class="abs benefit-pill" style="left:190px;top:370px"><i></i>Save<br>Costs</div>
  <div class="abs benefit-pill" style="left:310px;top:370px;font-size:5.6px"><i></i>Avoid<br>Inconveniences</div>

  <div class="abs detail-band"></div>
  <div class="abs detail" style="left:38px">
    <h3>BECOME MOBILE <span>▯</span></h3>
    <p>From our cloud-based telephony and its unified communications system emerges the concept of mobility. Make calls using your office phone, computer, or mobile phone, and chat with your colleagues and customers from numerous locations. Enjoy centralized communications and simplified management.</p>
  </div>
  <div class="abs detail" style="left:193px">
    <h3>SAVE COSTS <span>●</span></h3>
    <p>The fixed and operating costs of your business communications are substantially reduced, and we take care of installing, configuring, and managing your phone system. Call us today for free consultation</p>
  </div>
  <div class="abs detail" style="left:348px">
    <h3>STAY ABREAST <span>↗</span></h3>
    <p>Enjoy leading-edge telecommunications technology and its host of features that adapt to your needs, whatever the size of your business. These features are constantly upscaled and automatically updated. You will thus never have to operate an obsolete system.</p>
  </div>
  <div class="abs detail-wide">
    <h3>AVOID INCONVENIENCES <span>♛</span></h3>
    <p>We take charge of the structure of your business phone system and remove the PBX (Private Branch Exchange) system to host it in its cloud database, thus saving you space, time, and costs. You are cleared of wire clutter and your business communications are streamlined, allowing you to work freely and efficiently. Also, this service includes an excellent recovery and business continuity plan that prevents unforeseen events, such as claims or system failures, from leading to data loss or suspension of business activities.</p>
  </div>
</section>

</body>
</html>
```